Psychologe  sucht Corporate Design
Psychologe sucht Corporate Design
Sehr kreative und originelle Arbeit, alles worum ich gebeten habe wurde stets zeitnah umgesetzt. Nur die Kommunikation / Abstimmung war manchmal etwas mühsam.
Zielgruppe
Als Psychologe begleite ich Teams, Organisationen und Individuen bei Veränderungen.
Meine Zielgruppe sind überwiegend DAX-notierte Unternehmen, allerdings habe ich auch Kunden im Non-Profit-Bereich und wünsche mir daher, dass das Redesign meines Auftritts breit/offen genug bleibt, dass diese Klientel sich darin auch wieder findet.
Mein Portfolio umfasst die 'klassische' Trias aus Training, Coaching und Beratung. Darüber hinaus moderiere ich Veranstaltungen, von Klausur-Tagungen bis zu Change-Management-Workshops.
Aufgabenstellung
Ich wünsche mir ein Redesign meines bisherigen Auftritts. Das Logo soll im Kernelement erhalten bleiben. Das heißt, der Doppelpfeil der gemeinsam einen Kreis bildet sollte konstant bleiben. Alles andere darf frischer und vom insgesamten Layout 'zusammen-gehöriger' werden. Gerne dürfen die Pfeile an sich überarbeitet werden, mittlerweile finde ich sie fast ein bisschen zu standardmäßig, wie aus so einer WORD-Vorlage. Bisheriges Logo-Design ist als PDF angehängt oder auch auf meiner Homepage einsehbar: www.konrad-molbrecht.de
Das Desgin sollte hochwertig, klassisch und edel anmuten. Meine Angebote richten sich an eine finanzstarke Zielgruppe, die sich davon auch angesprochen fühlen sollte. Werte sind eher in Richtung Stabilität, Klarheit, Vertrauen und Seriösität.
Das Design soll max. ZWEI Farben enthalten. Die eine Farbe soll ein tiefer, eher dunkler Petrol-Türkis-Ton sein. Die andere Farbe soll passend dazu aus dem Spektrum Gelb - Orange - Rot sein. Ich bevorzuge insgesamt eher runde als eckige Formen, wobei es trotzdem Prägnanz haben sollte.
Das Logo soll insgesamt meinen Namen beinhalten und drunter 'Training & Coaching'. Dabei wünsche ich mir zwei Varianten: a) Logo oben drüber, b) Logo links und den Text rechts vom Logo. Die Schriften dürfen gerne vollständig überarbeitet werden. Hierbei eher klare, prägnante und wertvolle Schriften. Es darf auch bis hin zu etwas Schwungvollem gehen, ich bin offen für Vorschläge.

```html
<!DOCTYPE html>
<html lang="de">
<head>
<meta charset="utf-8">
<title>Konrad Molbrecht – Corporate Design</title>
<link href="https://fonts.googleapis.com/css2?family=Montserrat:wght@400;600&family=Arimo:wght@400;700&display=swap" rel="stylesheet">
<style>
  :root {
    --petrol: #0b3a5c;
    --petrol-deep: #082e4a;
    --petrol-soft: #1d4a6b;
    --accent: #e4532a;
    --paper: #ffffff;
    --paper-shade: #f3f3f4;
    --ink: #2b2b2b;
    --stage: #e7e8ea;
    --faint-mark: #d9e2ea;
  }
  * { box-sizing: border-box; margin: 0; padding: 0; }
  html, body { width: 1200px; height: 800px; overflow: hidden; }
  body {
    position: relative;
    background: var(--stage);
    font-family: "Arimo", Arial, sans-serif;
    color: var(--ink);
  }
  .sheet {
    position: absolute;
    background: linear-gradient(160deg, var(--paper) 40%, var(--paper-shade));
    box-shadow: 0 6px 18px rgba(0,0,0,.18);
    overflow: hidden;
  }
  .sheet--dark {
    background: linear-gradient(150deg, var(--petrol-soft), var(--petrol-deep) 70%);
  }

  /* brand lockup */
  .brand { display: inline-flex; flex-direction: column; align-items: center; }
  .brand__dot { border-radius: 50%; background: var(--accent); }
  .brand__name {
    font-family: "Montserrat", Arial, sans-serif;
    font-weight: 600;
    color: var(--petrol);
    white-space: nowrap;
    line-height: 1.1;
  }
  .brand__tagline {
    display: flex; align-items: center; gap: 6px;
    font-family: "Montserrat", Arial, sans-serif;
    font-weight: 400;
    color: var(--accent);
    white-space: nowrap;
  }
  .brand__tagline::before, .brand__tagline::after {
    content: ""; height: 1px; width: 22px; background: var(--accent);
  }
  .brand--sm .brand__dot { width: 18px; height: 18px; margin-bottom: 4px; }
  .brand--sm .brand__name { font-size: 11px; }
  .brand--sm .brand__tagline { font-size: 6.5px; margin-top: 2px; }
  .brand--lg .brand__dot { width: 62px; height: 62px; margin-bottom: 10px; }
  .brand--lg .brand__name { font-size: 22px; }
  .brand--lg .brand__tagline { font-size: 11px; margin-top: 4px; }
  .brand--lg .brand__tagline::before, .brand--lg .brand__tagline::after { width: 44px; }
  .brand--light .brand__name { color: var(--paper); }

  .bottom-band { position: absolute; left: 0; bottom: 0; width: 100%; display: block; }

  /* letterhead */
  .letterhead { left: 40px; top: 40px; width: 340px; height: 480px; }
  .letterhead .brand { position: absolute; left: 24px; top: 22px; }
  .letterhead__watermark {
    position: absolute; left: 118px; top: 150px;
    width: 180px; height: 180px; border-radius: 50%;
    background: var(--faint-mark); opacity: .7;
  }
  .letter {
    position: absolute; left: 56px; top: 120px; width: 236px;
    font-size: 6px; line-height: 1.5;
  }
  .letter p { margin-bottom: 6px; }
  .letter__sign { margin-top: 26px; }

  /* folder */
  .folder { left: 410px; top: 40px; width: 340px; height: 480px; border-radius: 0 6px 6px 0; }
  .folder__spine {
    position: absolute; left: 22px; top: 0; bottom: 0; width: 2px;
    background: rgba(0,0,0,.22);
  }
  .folder .brand { position: absolute; left: 50%; top: 50%; transform: translate(-50%, -50%); }

  /* business cards */
  .card { width: 370px; height: 215px; left: 790px; }
  .card--front { top: 40px; }
  .card--front .brand { position: absolute; left: 26px; top: 30px; }
  .card__contact {
    position: absolute; right: 28px; top: 92px;
    font-size: 10px; line-height: 1.6; text-align: left;
  }
  .card__contact dt { display: inline-block; width: 42px; color: var(--petrol); font-weight: 700; }
  .card__contact dd { display: inline; }
  .card__person { font-weight: 700; color: var(--petrol); margin-bottom: 4px; }
  .card--back { top: 280px; }
  .card--back .brand { position: absolute; left: 50%; top: 50%; transform: translate(-50%, -50%); }
  .card--back .brand__dot { width: 30px; height: 30px; }
  .card--back .brand__name { font-size: 15px; }
  .card--back .brand__tagline { font-size: 8px; }

  /* envelopes */
  .envelope { top: 540px; width: 520px; height: 230px; }
  .envelope--front { left: 40px; }
  .envelope--front .brand { position: absolute; left: 26px; top: 22px; }
  .envelope--back { left: 640px; }
  .envelope__flap { position: absolute; left: 0; top: 0; width: 100%; height: 100%; }
</style>
</head>
<body>
  <main class="stationery">

    <article class="sheet letterhead">
      <div class="brand brand--sm">
        <span class="brand__dot"></span>
        <span class="brand__name">Konrad Molbrecht</span>
        <span class="brand__tagline">Training &amp; Coaching</span>
      </div>
      <div class="letterhead__watermark"></div>
      <div class="letter">
        <p>21 January 2014</p>
        <p>Mara Dellweg<br>Level 2, 14 Harbor Lane<br>Portvale, NY 10400</p>
        <p>Dear friend,</p>
        <p>Following is a short note about our next workshop.</p>
        <p>Thank you for the open talks last week. We will meet again in spring to plan the team days and the review.</p>
        <p>Please send the list of topics and the dates that suit your group, and we will prepare the agenda.</p>
        <p>We look forward to working with you.</p>
        <p class="letter__sign">Yours faithfully<br><br>Lena Vorhold<br>Managing Director</p>
      </div>
      <svg class="bottom-band" viewBox="0 0 340 22" height="22" aria-hidden="true">
        <polygon points="0,12 176,12 184,22 0,22" fill="var(--petrol)"/>
        <polygon points="196,4 340,4 340,22 204,22" fill="var(--accent)"/>
      </svg>
    </article>

    <article class="sheet sheet--dark folder">
      <div class="folder__spine"></div>
      <div class="brand brand--lg brand--light">
        <span class="brand__dot"></span>
        <span class="brand__name">Konrad Molbrecht</span>
        <span class="brand__tagline">Training &amp; Coaching</span>
      </div>
    </article>

    <article class="sheet card card--front">
      <div class="brand brand--sm">
        <span class="brand__dot"></span>
        <span class="brand__name">Konrad Molbrecht</span>
        <span class="brand__tagline">Training &amp; Coaching</span>
      </div>
      <div class="card__contact">
        <div class="card__person">Level 1, 2 Harbor Lane<br>Portvale, NY 10400</div>
        <dl>
          <dt>phone</dt><dd>555 014 7720</dd><br>
          <dt>email</dt><dd>lena@konrad-molbrecht.de</dd><br>
          <dt>web</dt><dd>konrad-molbrecht.de</dd>
        </dl>
      </div>
      <svg class="bottom-band" viewBox="0 0 370 20" height="20" aria-hidden="true">
        <polygon points="0,11 150,11 158,20 0,20" fill="var(--petrol)"/>
        <polygon points="170,4 370,4 370,20 178,20" fill="var(--accent)"/>
      </svg>
    </article>

    <article class="sheet sheet--dark card card--back">
      <div class="brand brand--sm brand--light">
        <span class="brand__dot"></span>
        <span class="brand__name">Konrad Molbrecht</span>
        <span class="brand__tagline">Training &amp; Coaching</span>
      </div>
    </article>

    <article class="sheet envelope envelope--front">
      <div class="brand brand--sm">
        <span class="brand__dot"></span>
        <span class="brand__name">Konrad Molbrecht</span>
        <span class="brand__tagline">Training &amp; Coaching</span>
      </div>
    </article>

    <article class="sheet envelope envelope--back">
      <svg class="envelope__flap" viewBox="0 0 520 230" preserveAspectRatio="none" aria-hidden="true">
        <polygon points="0,0 520,0 520,92 24,92 0,70" fill="var(--petrol)"/>
      </svg>
    </article>

  </main>
</body>
</html>
```